New Generation Winery needs inspiring label for special bottling

We are a family owned winery in the Rhine Valley in Germany. Check www.brendel-aumann.de . We have a very exciting project going: In 2014 we harvested our best vinyard and split the grapes in half. First half I have treated the way I have done it over the past 40 years. Second half I gave to my daughter who is just entering the winemaking business. She has treated it in a completely different way - her way - the way of the new generation. One of the differentiators; she has squeezed the juices with her bare feet which reduces acidity and bitterness in the wine (less tannins). This is why we want to call the wine "Mondgrüße" (meaning "Moongreets"). Please be careful when writing the "ß" . It is a German letter which replaces the "double s". It is NOT a capital B!! I Have attached a file which gives you the size of the label and another file which shows the current design of the winery labels. If possible it should pick up some elements from the current design (maybe just the colours?) but otherwise you are free. It will go on a dark green bottle, almost black. Apart from the word "Mondgrüße" you need to place the grape "Riesling", the word "trocken" (means dry) and the year of the harvest "2014".

Industry/Entity Type

Brendel

Requirements
Nice to have
• Update 25.3.2015: Have a look at the attached image "Inspiration". Maybe that is a good thought starter, too. Have fun..

```html
<!DOCTYPE html>
<html lang="de">
<head>
<meta charset="utf-8">
<title>Mondgrüße – Riesling trocken 2014</title>
<link href="https://fonts.googleapis.com/css2?family=Playfair+Display:wght@400&family=Raleway:wght@500&family=Libre+Baskerville&display=swap" rel="stylesheet">
<style>
  :root {
    --page: #ffffff;
    --ink: #173446;
    --silver-light: #f4f4f4;
    --silver-mid: #d9d9d9;
    --silver-dark: #b9b9b9;
    --wash-olive: #a8a12a;
    --wash-lime: #c9c43a;
    --wash-moss: #7f7d22;
    --year-box: #14344a;
    --year-text: #f2f2f2;
  }
  html, body {
    margin: 0;
    padding: 0;
    width: 1200px;
    height: 1000px;
    overflow: hidden;
    background: var(--page);
  }
  .canvas {
    position: relative;
    width: 1200px;
    height: 1000px;
  }
  .label {
    position: absolute;
    left: 240px;
    top: 100px;
    width: 720px;
    height: 800px;
    overflow: hidden;
    background: linear-gradient(90deg,
      var(--silver-dark) 0%,
      var(--silver-mid) 12%,
      var(--silver-light) 45%,
      var(--silver-light) 60%,
      var(--silver-mid) 88%,
      var(--silver-dark) 100%);
  }
  .watercolour-wash {
    position: absolute;
    left: 0;
    top: 0;
    width: 720px;
    height: 560px;
  }
  .wine-name {
    position: absolute;
    left: 0;
    right: 0;
    top: 325px;
    margin: 0;
    text-align: center;
    font-family: "Playfair Display", serif;
    font-weight: 400;
    font-size: 94px;
    line-height: 1;
    color: var(--ink);
    letter-spacing: 1px;
  }
  .wine-style {
    position: absolute;
    left: 0;
    right: 0;
    top: 462px;
    margin: 0;
    display: flex;
    justify-content: center;
    align-items: center;
    gap: 16px;
    font-family: "Raleway", sans-serif;
    font-weight: 500;
    font-size: 31px;
    letter-spacing: 1.5px;
    color: var(--ink);
  }
  .wine-style .dash {
    display: block;
    width: 52px;
    height: 2px;
    background: var(--ink);
  }
  .winery-name {
    position: absolute;
    left: 0;
    right: 0;
    top: 622px;
    margin: 0;
    text-align: center;
    font-family: "Libre Baskerville", serif;
    font-size: 22px;
    letter-spacing: 0.5px;
    color: var(--ink);
  }
  .vintage {
    position: absolute;
    left: 302px;
    top: 713px;
    width: 108px;
    height: 87px;
    background: var(--year-box);
    color: var(--year-text);
    font-family: "Libre Baskerville", serif;
    font-size: 24px;
    letter-spacing: 1px;
    display: flex;
    align-items: center;
    justify-content: center;
  }
</style>
</head>
<body>
<main class="canvas">
  <section class="label">
    <svg class="watercolour-wash" viewBox="0 0 720 560" role="img" aria-label="Yellow-green watercolour wash with white bare footprints walking across it">
      <defs>
        <radialGradient id="washCore" cx="50%" cy="42%" r="60%">
          <stop offset="0%" stop-color="var(--wash-lime)"/>
          <stop offset="55%" stop-color="var(--wash-olive)"/>
          <stop offset="100%" stop-color="var(--wash-moss)" stop-opacity="0.55"/>
        </radialGradient>
        <linearGradient id="washFade" x1="0" y1="0" x2="0" y2="1">
          <stop offset="0%" stop-color="#fff" stop-opacity="1"/>
          <stop offset="72%" stop-color="#fff" stop-opacity="1"/>
          <stop offset="100%" stop-color="#fff" stop-opacity="0"/>
        </linearGradient>
        <mask id="washMask">
          <rect width="720" height="560" fill="url(#washFade)"/>
        </mask>
      </defs>
      <rect width="720" height="560" fill="url(#washCore)" mask="url(#washMask)"/>
    </svg>

    <h1 class="wine-name">Mondgrüße</h1>
    <p class="wine-style"><span>TROCKEN</span><span class="dash"></span><span>RIESLING</span></p>
    <p class="winery-name">BRENDEL-AUMANN</p>
    <div class="vintage">2014</div>
  </section>
</main>
</body>
</html>
```